Verdant Medispa Business Card

need a business card for our medispa, attached please see the logo.
our website is https://verdantmedispa-example.com

Sorina Belcourt, MD
Internal Medicine

555-204-7193

Sorina@verdantmedispa-example.com

Www.Verdantmedispa-example.com

738 E Harlow Blvd N, Ste 512, Katy, TX 77981

Target Market(s)

MedSpa, Cosmetics, Esthetics

Industry/Entity Type

MedicalSpa

Contact Information for Business Card

Please see the attached business card which i pulled from the internet. I like the idea back as a logo and front with info.

Font styles to use
Decorative

Requirements
Must have
• Color should be matching with Logo and Website theme, Also I like to have QR code for the website

```html
<!DOCTYPE html>
<html lang="en">
<head>
<meta charset="utf-8">
<title>Verdant Medispa Business Card</title>
<link rel="stylesheet" href="https://fonts.googleapis.com/css2?family=Cinzel:wght@600&family=Roboto:wght@400&display=swap">
<style>
  :root {
    --page: #ffffff;
    --card: #ffffff;
    --gold: #d4a92c;
    --gold-deep: #b98d1e;
    --gold-light: #f1d654;
    --gold-back: #d9b640;
    --ink: #1f1f1f;
    --qr-field: #fbf3d6;
  }
  * { margin: 0; padding: 0; box-sizing: border-box; }
  html, body {
    width: 1200px; height: 896px; overflow: hidden;
    background: var(--page);
  }
  .canvas { position: relative; width: 1200px; height: 896px; }
  .card {
    position: absolute; left: 334px; width: 527px; height: 302px;
    border-radius: 24px; overflow: hidden;
  }
  .card--front { top: 124px; background: var(--card); border: 1px solid #ececec; }
  .card--back { top: 471px; background: var(--gold-back); }

  .brand {
    position: absolute; left: 0; right: 0; text-align: center;
    font-family: "Cinzel", serif; font-weight: 600; color: var(--gold);
    letter-spacing: 2px; white-space: nowrap;
  }
  .card--front .brand { top: 58px; font-size: 40px; }
  .card--back .brand { top: 122px; font-size: 46px; color: var(--gold-deep); }
  .brand__mark {
    display: inline-block; width: 12px; height: 12px; border-radius: 50%;
    background: currentColor; vertical-align: middle; margin-right: 12px;
  }

  .holder {
    position: absolute; left: 44px; top: 178px; width: 208px; text-align: right;
  }
  .holder__name {
    font-family: "Cinzel", serif; font-weight: 600; font-size: 18.5px;
    color: var(--gold); white-space: nowrap; letter-spacing: 0.2px;
  }
  .holder__role {
    margin-top: 18px; font-family: "Roboto", sans-serif; font-size: 12.5px; color: var(--ink);
  }
  .divider {
    position: absolute; left: 263px; top: 181px; width: 1.5px; height: 54px;
    background: var(--gold);
  }
  .contacts {
    position: absolute; left: 273px; top: 178px; list-style: none;
    font-family: "Roboto", sans-serif; font-size: 12.5px; color: var(--ink);
  }
  .contacts li { display: flex; align-items: center; height: 20px; gap: 3px; white-space: nowrap; }
  .contacts svg { width: 11px; height: 11px; flex: none; }

  .address-band {
    position: absolute; left: 0; right: 0; top: 267px; height: 18px;
    background: linear-gradient(180deg, var(--gold-light) 0%, var(--gold) 45%, var(--gold-deep) 100%);
    font-family: "Roboto", sans-serif; font-size: 12.5px; color: var(--ink);
    text-align: center; line-height: 18px; white-space: nowrap;
  }

  .website-qr {
    position: absolute; right: 24px; bottom: 24px; width: 58px; height: 58px;
    background: var(--qr-field); border: 3px solid var(--gold-deep); border-radius: 4px;
  }
</style>
</head>
<body>
<main class="canvas">
  <section class="card card--front" aria-label="Card front">
    <div class="brand"><span class="brand__mark"></span>Verdant Medispa</div>

    <div class="holder">
      <div class="holder__name">Sorina Belcourt, MD</div>
      <div class="holder__role">Internal Medicine</div>
    </div>
    <div class="divider"></div>

    <ul class="contacts">
      <li>
        <svg viewBox="0 0 24 24" aria-hidden="true"><path fill="var(--gold)" d="M6.6 10.8a15 15 0 0 0 6.6 6.6l2.2-2.2c.3-.3.7-.4 1-.2 1.1.4 2.3.6 3.6.6.6 0 1 .4 1 1V20c0 .6-.4 1-1 1A17 17 0 0 1 3 4c0-.6.4-1 1-1h3.5c.6 0 1 .4 1 1 0 1.3.2 2.5.6 3.6.1.3 0 .7-.2 1z"/></svg>
        555-204-7193
      </li>
      <li>
        <svg viewBox="0 0 24 24" aria-hidden="true"><rect x="2" y="5" width="20" height="14" rx="1" fill="var(--gold)"/><path d="M3 6l9 7 9-7" fill="none" stroke="#fff" stroke-width="1.6"/></svg>
        Sorina@verdantmedispa-example.com
      </li>
      <li>
        <svg viewBox="0 0 24 24" aria-hidden="true"><circle cx="12" cy="12" r="10" fill="var(--gold)"/><path d="M2 12h20M12 2c3 3 3 17 0 20M12 2c-3 3-3 17 0 20" fill="none" stroke="#fff" stroke-width="1.3"/></svg>
        Www.Verdantmedispa-example.com
      </li>
    </ul>

    <div class="address-band">738 E Harlow Blvd N, Ste 512, Katy, TX 77981</div>
  </section>

  <section class="card card--back" aria-label="Card back">
    <div class="brand"><span class="brand__mark"></span>Verdant Medispa</div>
    <div class="website-qr" role="img" aria-label="QR code linking to https://verdantmedispa-example.com"></div>
  </section>
</main>
</body>
</html>
```